Web Design Project

This as the foundation http://fenlarkstudio.com/demo_viewer/index.php?theme=vostriquewp

Site needs to have a glossy black background with white text…..Extremely modern with a few flares of pallor 5 style but nothing too off the wall, easily understood.

Here are some other reference sites and likes and dislikes that will help: (Probably overkill but we are looking for a cutting edge New York / LA Style )

http://www.brevinandcrewtx.com

Like- The black background with white font is very eye catching and clean. Love the contrast. Black is a great background for photographs and videos

http://maltegrunow.com

Like- Clean homepage, black and white color scheme works well.

http://orvillekastnerphotography.com

Like- Nice Menu, nice B and W contrast

http://www.qvx.com

Like- Like the Menu. Clean and easy.

http://www.saffelmedia.com

Like- Contrast of white background with black font.

Like- Slide show of stills (but should be able to click images to go to video. We’d also like the name of the project)

Like- Drop down menu allows for customer to find service they need without going through all services.

Like- Tells you work that they do right next to the logo.

Dislike- Too much information on homepage. Too much scrolling.

http://www.tundravoxfilms.com

Like- High Res images on home page

Like - The About Me is on homepage and speaks to potential customer directly. “We create award-winning videos for companies like yours.”

Like- Blog is updated with new projects they do. And short, visual entries

Like- “Work” section stands out from website. The background fades to light grey and white when you click on “work” so that the portfolio stands out more. Makes color look more vivid

Like- Black and white color scheme with grey header

http://www.bureau847.com

Like- High Res images on home page pointing to projects

Like- Photograph as background, changes with different links. So work is always showcased and creates contrast. Information is laid over a barely translucent background, which is laid over the picture.

Like- They have a good Attitude about quality of their product

http://www.quillmarsh.net

Like- First thing you see when open page is a clear big statement about what they do, said in a catchy way. They have a Tagline.

http://plinthworks.com

Like- How work is categorized. Client list has links, which take you to their Client page with all their work grouped together. Nice flow and organization shows client relationships. And nice descriptions of what the job was and how it was executed… Way too wordy at times though

http://www.marisadoneimages.com

Like- The homepage is very clean and accessible. Love the color scheme and how Logo is centered between the links.

Of the four designs we have gotten EVERY SINGLE ONE has been a template STOLEN from another site. We are paying for ORIGINAL design. Not copies and templates. Please ONLY submit original designs

```html
<!DOCTYPE html>
<html lang="en">
<head>
<meta charset="utf-8">
<title>Marrowlane Productions</title>
<link href="https://fonts.googleapis.com/css2?family=Anton&family=Open+Sans:wght@400;600;700&display=swap" rel="stylesheet">
<style>
:root{
  --ink:#f2f2f2;
  --text:#d6d6d6;
  --muted:#8c8c8c;
  --soft:#6e6e6e;
  --header-bg:linear-gradient(180deg,#1c1c1c 0%,#0b0b0b 55%,#050505 100%);
  --band-bg:linear-gradient(180deg,#0a0a0a 0%,#000 100%);
  --body-bg:linear-gradient(180deg,#121212 0%,#070707 100%);
  --side-bg:#050505;
  --footer-bg:linear-gradient(180deg,#171717 0%,#0c0c0c 100%);
  --line:#2a2a2a;
  --black:#000;
  --white:#fff;
  --accent:#1aa3d9;
}
*{box-sizing:border-box;margin:0;padding:0}
html,body{width:1200px;height:1000px;overflow:hidden}
body{position:relative;background:#0a0a0a;font-family:"Open Sans",Arial,sans-serif;color:var(--ink)}
.display{font-family:"Anton","Oswald",Impact,sans-serif;font-weight:400;text-transform:uppercase}
.abs{position:absolute}

.top-rule{left:0;top:0;width:1200px;height:5px;background:#2a2a2a}
.site-header{left:0;top:5px;width:1200px;height:115px;background:var(--header-bg);border-bottom:1px solid var(--line)}
.brand{left:300px;top:42px;display:flex;align-items:center;gap:10px;font-size:22px;color:var(--white);letter-spacing:.5px}
.brand-mark{width:26px;height:26px;border:2px solid var(--white);border-radius:50%}
.search{left:716px;top:47px;width:160px;height:23px;border:1px solid #333;background:#141414;font-size:8px;color:#999;padding:6px 9px}
.search svg{position:absolute;right:10px;top:6px}
.social{left:811px;top:80px;display:flex;gap:3px}
.social span{width:10px;height:10px;background:#5a5a5a;border-radius:2px}

.hero{left:0;top:120px;width:1200px;height:281px;background:var(--band-bg);border-bottom:1px solid var(--line)}
.main-nav{left:296px;top:143px;list-style:none;font-size:17.5px;line-height:18.4px;color:var(--white)}
.main-nav .current{color:var(--muted)}
.video{left:493px;top:137px;width:383px;height:247px;background:radial-gradient(ellipse at 50% 40%,#b08a6a 0%,#6a5546 35%,#2a3440 75%,#1d2a36 100%)}
.video-title{left:516px;top:158px;display:flex;gap:6px}
.video-title .thumb{width:38px;height:38px;background:#111}
.video-title .tag{font-size:10px;font-weight:700;background:#111;color:var(--accent);padding:0 3px;line-height:13px;display:inline-block}
.video-title .from{font-size:7px;color:#ddd;background:#111;padding:1px 3px;margin-top:2px}
.video-title .from b{color:var(--accent);font-weight:600}
.video-actions{left:833px;top:157px;display:flex;flex-direction:column;gap:5px}
.video-actions div{width:27px;height:21px;background:rgba(0,0,0,.75);border-radius:2px;color:#fff;font-size:4.5px;font-weight:700;text-align:center;padding-top:3px}
.video-actions svg{display:block;margin:0 auto 1px}
.player{left:518px;top:338px;width:334px;height:22px;background:rgba(0,0,0,.8);border-radius:2px}
.play-btn{left:518px;top:338px;width:40px;height:22px;background:#111;border-radius:2px}
.track{left:570px;top:346px;width:210px;height:6px;background:#555;border:1px solid #888}
.track i{position:absolute;left:0;top:0;height:4px;width:60px;background:var(--accent)}
.hd{left:812px;top:343px;font-size:10px;font-weight:700;font-style:italic;color:var(--accent)}

.main-bg{left:0;top:401px;width:1200px;height:511px;background:var(--body-bg)}
.content-frame{left:93px;top:401px;width:986px;height:511px;border-left:1px solid var(--line);border-right:1px solid var(--line)}
.side-left{left:0;top:401px;width:93px;height:511px;background:var(--side-bg)}
.side-right{left:1079px;top:401px;width:121px;height:511px;background:var(--side-bg)}
.tagline{left:0;top:428px;width:1172px;text-align:center;font-size:18.4px;font-weight:700;color:var(--white)}
.welcome{left:296px;top:466px;line-height:26px}
.welcome .lead{font-family:"Open Sans",sans-serif;font-weight:700;font-size:25px;color:var(--soft);letter-spacing:-.3px}
.welcome .name{font-size:27px;line-height:28px;color:var(--white);margin-top:1px}
.divider{left:481px;top:468px;width:1px;height:100px;background:var(--line)}
.intro{left:493px;top:469px;width:380px;font-size:9.1px;line-height:13.6px;color:var(--text);letter-spacing:-.08px}
.intro strong{display:block;margin-bottom:7px;font-weight:700;color:var(--white)}

.section-head{font-size:17.5px;color:var(--white);display:flex;gap:16px}
.section-head .more{color:var(--soft)}
.featured-head{left:296px;top:603px}
.project{top:646px;width:184px;height:72px}
.project .shot{position:absolute;inset:0}
.project .label{position:absolute;left:0;top:37px;background:rgba(0,0,0,.85);color:#fff;font-size:12px;padding:3px 6px;text-transform:none;letter-spacing:.1px}
.p1{left:297px}.p1 .shot{background:linear-gradient(90deg,#3a3530,#6d6458 50%,#2c2824)}
.p2{left:494px}.p2 .shot{background:linear-gradient(90deg,#8e6a58,#c99a82 50%,#7a5a4c)}
.p3{left:691px}.p3 .shot{background:linear-gradient(90deg,#8a5a2a,#5a3420 55%,#2b1a12)}
.arrow{top:675px}

.blog-head{left:296px;top:758px}
.post{top:800px;width:190px}
.post .thumb{position:absolute;left:0;top:0;width:37px;height:34px}
.post h3{position:absolute;left:50px;top:-1px;width:140px;font-size:12.5px;line-height:14px;text-transform:none;color:var(--white)}
.post p{position:absolute;left:50px;top:34px;width:142px;font-size:8.9px;line-height:13.8px;color:var(--text)}
.post p b{font-weight:700;color:var(--white)}
.post1{left:296px}.post1 .thumb{background:linear-gradient(135deg,#c46a4a,#e0b090)}
.post2{left:493px}.post2 .thumb{background:linear-gradient(135deg,#3a5a7a,#c0a070)}
.quote-cta{left:691px;top:801px;width:185px;height:78px;background:#2e2e2e;padding:6px}
.quote-cta .inner{width:100%;height:100%;background:var(--white);color:var(--black);display:flex;align-items:center;gap:12px;padding-left:14px;font-size:16.5px;line-height:16px}

.site-footer{left:0;top:912px;width:1200px;height:88px;background:var(--footer-bg);border-top:1px solid var(--line)}
.copyright{left:296px;top:936px;font-size:8.5px;color:var(--muted)}
</style>
</head>
<body>
<div class="abs top-rule"></div>

<header class="abs site-header"></header>
<div class="abs brand"><span class="brand-mark"></span><span>Marrowlane Productions</span></div>
<div class="abs search">Search Here...
  <svg width="10" height="10" viewBox="0 0 10 10"><circle cx="4" cy="4" r="3" fill="none" stroke="#aaa" stroke-width="1.4"/><line x1="6.2" y1="6.2" x2="9" y2="9" stroke="#aaa" stroke-width="1.6"/></svg>
</div>
<div class="abs social"><span></span><span></span><span></span><span></span><span></span></div>

<section class="abs hero"></section>
<ul class="abs main-nav display">
  <li class="current">Home</li><li>Services</li><li>Video Gallery</li><li>About Us</li><li>Contact Us</li><li>Show Reel</li><li>Actor Demo Reels</li><li>Video Blog</li><li>Client List</li><li>Client Testimonials</li><li>Photo Gallery</li><li>FAQ</li>
</ul>
<div class="abs video" role="img" aria-label="Showreel video still of a model in a fur hat"></div>
<div class="abs video-title">
  <div class="thumb"></div>
  <div><span class="tag">STYLE</span><div class="from">from <b>Marrowlane Productions</b></div></div>
</div>
<div class="abs video-actions">
  <div><svg width="9" height="8" viewBox="0 0 10 9"><path d="M5 9 0.8 4.6A2.4 2.4 0 0 1 5 1.4 2.4 2.4 0 0 1 9.2 4.6Z" fill="#fff"/></svg>LIKE</div>
  <div><svg width="9" height="9" viewBox="0 0 10 10"><circle cx="5" cy="5" r="4" fill="none" stroke="#fff" stroke-width="1.2"/><path d="M5 2.5V5h2" fill="none" stroke="#fff" stroke-width="1.2"/></svg>LATER</div>
  <div><svg width="9" height="9" viewBox="0 0 10 10"><path d="M1 9 5 4 9 1M6 1h3v3" fill="none" stroke="#fff" stroke-width="1.3"/></svg>SHARE</div>
  <div><svg width="10" height="8" viewBox="0 0 12 8"><path d="M4 1 1 4l3 3M8 1l3 3-3 3M7 0 5 8" fill="none" stroke="#fff" stroke-width="1.2"/></svg>EMBED</div>
</div>
<div class="abs player"></div>
<div class="abs play-btn"><svg width="40" height="22" viewBox="0 0 40 22"><path d="M16 6v10l9-5Z" fill="#fff"/></svg></div>
<div class="abs track"><i></i></div>
<svg class="abs" style="left:786px;top:346px" width="22" height="7" viewBox="0 0 22 7"><g fill="#1aa3d9"><rect x="0" width="2" height="7"/><rect x="4" width="2" height="7"/><rect x="8" width="2" height="7"/><rect x="12" width="2" height="7"/><rect x="16" width="2" height="7"/></g></svg>
<div class="abs hd">HD</div>
<svg class="abs" style="left:833px;top:345px" width="8" height="8" viewBox="0 0 8 8"><path d="M0 0h3L0 3ZM8 0v3L5 0ZM0 8V5l3 3ZM8 8H5l3-3Z" fill="#fff"/></svg>

<div class="abs main-bg"></div>
<div class="abs side-left"></div>
<div class="abs side-right"></div>
<div class="abs content-frame"></div>

<p class="abs tagline">“We create award-winning videos for companies like yours.”</p>
<h1 class="abs welcome"><span class="lead">WELCOME TO</span><div class="name display">Marrowlane<br>Productions</div></h1>
<div class="abs divider"></div>
<div class="abs intro">
  <strong>We are Marrowlane Production lorem ipsum dolor sit amet, consectetur adipiscing elit. Quisque posuere feugiat gravida. Sed fringilla velit vitae commodo condimentum</strong>
  Donec euismod laoreet lorem at auctor. Vestibulum nec laoreet ipsum. Nam neque felis, euismod sed diam ac, euismod interdum urna. Mauris tincidunt feugiat viverra. Pellentesque vehicula nunc ac luctus condimentum. Morbi id libero sed leo hendrerit bibendum. Pellen-tesque malesuada diam libero, eu elementum urna venenatis in.
</div>

<h2 class="abs section-head featured-head display"><span>Featured Projects</span><span class="more">View All</span></h2>
<svg class="abs arrow" style="left:270px" width="12" height="16" viewBox="0 0 12 16"><path d="M10 2 4 8l6 6" fill="none" stroke="#eee" stroke-width="3"/></svg>
<div class="abs project p1"><div class="shot" role="img" aria-label="Project still of two men in a city street"></div><span class="label display">Project Title Here..</span></div>
<div class="abs project p2"><div class="shot" role="img" aria-label="Project still of a vintage styled portrait"></div><span class="label display">Project Title Here..</span></div>
<div class="abs project p3"><div class="shot" role="img" aria-label="Project still of a man in warm light"></div><span class="label display">Project Title Here..</span></div>
<svg class="abs arrow" style="left:889px" width="12" height="16" viewBox="0 0 12 16"><path d="M2 2l6 6-6 6" fill="none" stroke="#eee" stroke-width="3"/></svg>

<h2 class="abs section-head blog-head display"><span>Latest Blog</span><span class="more">Read More</span></h2>
<article class="abs post post1">
  <div class="thumb" role="img" aria-label="Blog thumbnail photo"></div>
  <h3 class="display">Sed et leo sollicitudin velit suscipit lacinia</h3>
  <p>Nam non adipiscing lectus. Quisque tempor nibh vel placerat posuere... <b>READ MORE</b></p>
</article>
<article class="abs post post2">
  <div class="thumb" role="img" aria-label="Blog thumbnail photo"></div>
  <h3 class="display">Sed et leo sollicitudin velit suscipit lacinia</h3>
  <p>Nam non adipiscing lectus. Quisque tempor nibh vel placerat posuere... <b>READ MORE</b></p>
</article>
<div class="abs quote-cta">
  <div class="inner display">
    <svg width="18" height="14" viewBox="0 0 18 14"><rect x="1" y="1" width="16" height="12" fill="none" stroke="#000" stroke-width="1.6"/><path d="M1 1.5 9 8l8-6.5" fill="none" stroke="#000" stroke-width="1.6"/></svg>
    <span>Contact Us<br>For a Free Quote</span>
  </div>
</div>

<footer class="abs site-footer"></footer>
<p class="abs copyright">Copyright © 2013 Marrowlane Productions. All rights reserved.</p>
</body>
</html>
```